Webdesign for development of custom specific electronics
Zielgruppe
We are specialised in development of custom specific electronics.
We also produce and test the pcb assemblies for our customers .
We sell some of our own products as well.
Aufgabenstellung
We provide an detailed briefing in a separate file.

```html
<!DOCTYPE html>
<html lang="de">
<head>
<meta charset="utf-8">
<title>Trusk Halvorsen – Elektronikentwicklung</title>
<link rel="stylesheet" href="https://fonts.googleapis.com/css2?family=Barlow:wght@400;500;600;700&display=swap">
<style>
:root{
  --bg-header:#1e1e1e;
  --bg-offer:#222222;
  --bg-product:#000000;
  --bg-footer:#111111;
  --card-dark:#333333;
  --orange:#ff6a00;
  --white:#ffffff;
  --muted:#c8c8c8;
  --navy:#0b1f3a;
  --blue-a:#2f95d5;
  --blue-b:#2cb6ea;
}
*{box-sizing:border-box;margin:0;padding:0}
html,body{width:1200px;height:2724px;overflow:hidden;background:var(--bg-header);font-family:"Barlow",Arial,sans-serif;color:var(--white)}
.section{position:absolute;left:0;width:1200px}
.abs{position:absolute}
.btn{position:absolute;display:flex;align-items:center;gap:12px;background:var(--orange);color:var(--white);font-weight:600;font-size:17px;padding:0 17px;height:42px}
.btn svg{width:16px;height:16px}

/* header */
.site-header{top:0;height:149px;background:var(--bg-header)}
.brand{left:97px;top:56px;display:flex;align-items:center;gap:12px;font-size:28px;font-weight:600;letter-spacing:.5px}
.brand-mark{width:22px;height:22px;background:#2aa8e0}
.main-nav{right:105px;top:70px;display:flex;gap:26px;font-size:17px;font-weight:600}

/* hero */
.hero{top:149px;height:534px;background:radial-gradient(ellipse at 60% 30%,#1f4a5c 0%,#10262f 45%,#070b0d 100%)}
.hero-photo{position:absolute;inset:0}
.hero-cta{right:105px;top:0}
.eyebrow{color:var(--orange);font-size:19px;font-weight:500}
.hero .eyebrow{left:106px;top:213px}
.hero-title{left:106px;top:252px;font-size:43px;line-height:51px;font-weight:700;width:760px}
.hero-text{left:106px;top:370px;font-size:18px;line-height:27px;width:760px;font-weight:500}

/* offer */
.offer{top:683px;height:705px;background:var(--bg-offer)}
.section-title{font-size:36px;font-weight:600}
.offer .section-title{left:106px;top:85px}
.card{position:absolute;overflow:hidden}
.card-production{left:106px;top:156px;width:315px;height:222px;background:linear-gradient(135deg,#3a8fd8,#2fa3e3)}
.card-service{left:106px;top:399px;width:315px;height:222px;background:var(--card-dark)}
.card-development{left:442px;top:156px;width:653px;height:465px;background:linear-gradient(135deg,#1e3f8a,#2459b8 50%,#162c5e)}
.card .btn{left:0;top:0}
.card-service p{position:absolute;left:17px;bottom:18px;font-size:19px;line-height:27px;width:260px}

/* product slider */
.product{top:1388px;height:568px;background:var(--bg-product)}
.product .eyebrow{left:106px;top:80px}
.product-title{left:106px;top:127px;font-size:37px;line-height:38px;font-weight:700;width:520px}
.product-text{left:106px;top:276px;font-size:19px;line-height:27px;width:560px;font-weight:500}
.product .btn{left:106px;top:420px}
.product-photo{left:694px;top:84px;width:401px;height:400px;background:radial-gradient(circle at 60% 45%,#3a3a3a,#161616 70%)}
.slider-arrow{top:272px;width:20px;height:28px}
.slider-prev{left:42px}
.slider-next{left:1139px}

/* philosophy */
.philosophy{top:1956px;height:468px;background:linear-gradient(90deg,var(--blue-a),var(--blue-b))}
.philosophy .section-title{left:95px;top:84px}
.philosophy-text{left:95px;top:150px;width:1000px;font-size:19px;line-height:27px;font-weight:500}
.philosophy-text p+p{margin-top:27px}
.philosophy-text a{color:var(--navy);text-decoration:none}

/* footer */
.site-footer{top:2424px;height:300px;background:var(--bg-footer)}
.footer-brand{left:100px;top:100px;font-size:19px;font-weight:600;width:168px;text-align:center}
.social{top:142px;display:flex;gap:18px;left:133px}
.social span{width:42px;height:42px;border:2px solid #8a8a8a;border-radius:50%}
.footer-info{left:357px;top:44px;font-size:12.5px;line-height:19px;color:var(--muted)}
.footer-info strong{color:var(--white);font-weight:600}
.footer-info p{margin-bottom:10px}
.footer-links{display:flex;gap:15px;color:var(--white);font-weight:600}
.map{left:611px;top:0;width:589px;height:300px;background:linear-gradient(135deg,#2e2e2e,#1d1d1d)}
.map-label{left:217px;top:26px;background:var(--orange);font-size:12.5px;line-height:17px;padding:6px 13px;font-weight:600}
.map-label span{font-weight:400}
</style>
</head>
<body>

<header class="section site-header">
  <div class="abs brand"><span class="brand-mark"></span>Trusk Halvorsen</div>
  <nav class="abs main-nav">
    <span>Entwicklung</span><span>Produktion</span><span>Service</span><span>Kontakt</span><span>Über uns</span>
  </nav>
</header>

<section class="section hero">
  <div class="hero-photo" role="img" aria-label="Nahaufnahme einer dunklen Leiterplatte mit Quarz und Chips"></div>
  <a class="btn hero-cta">Unsere One-Stop Angebote
    <svg viewBox="0 0 16 16" fill="none" stroke="#fff" stroke-width="2"><path d="M2 8h12M9 3l5 5-5 5"/></svg></a>
  <div class="abs eyebrow">Elektronikentwicklung und Fertigung von Schaltungen &amp; Baugruppen</div>
  <h1 class="abs hero-title">Innovative, qualitativ hochwertige und bezahlbare Produkte</h1>
  <p class="abs hero-text">Willkommen in der Welt der Elektronik. Neben unserem Kerngeschäft, der Fertigung- und Entwicklung von Eigen- und OEM Produkten, bieten wir auch die Entwicklung von kundenspezifischen Lösungen an.</p>
</section>

<section class="section offer">
  <h2 class="abs section-title">Unser Angebot</h2>
  <div class="card card-production" role="img" aria-label="Blaue Fläche mit Gittermuster">
    <a class="btn">Produktion <svg viewBox="0 0 16 16" fill="none" stroke="#fff" stroke-width="2"><path d="M2 8h12M9 3l5 5-5 5"/></svg></a>
  </div>
  <div class="card card-service">
    <a class="btn">Unser Service <svg viewBox="0 0 16 16" fill="none" stroke="#fff" stroke-width="2"><path d="M2 8h12M9 3l5 5-5 5"/></svg></a>
    <p>Wir bieten ihnen eine uneingeschränkte 5-jährige Zufriedenheitsgarantie.</p>
  </div>
  <div class="card card-development" role="img" aria-label="Lötkolben über blauen bestückten Leiterplatten">
    <a class="btn">Entwicklung <svg viewBox="0 0 16 16" fill="none" stroke="#fff" stroke-width="2"><path d="M2 8h12M9 3l5 5-5 5"/></svg></a>
  </div>
</section>

<section class="section product">
  <svg class="abs slider-arrow slider-prev" viewBox="0 0 20 28" fill="none" stroke="#ff6a00" stroke-width="3.5"><path d="M15 3L5 14l10 11"/></svg>
  <div class="abs eyebrow">Produkt ABC</div>
  <h2 class="abs product-title">Lorem ipsum dolor sit amet consectetur adipisicing do eiusmod</h2>
  <p class="abs product-text">Dolore magna aliqua. Ut enim ad minim dolore eu fugiat nulla pariatur veniam, quis nostrud exercitation ullamco Lorem ipsum incididunt ut labore et laboris nisi ut aliquip ex ea commodo cillum. Excepteur dolor sit amet.</p>
  <a class="btn">Mehr erfahren <svg viewBox="0 0 16 16" fill="none" stroke="#fff" stroke-width="2"><path d="M2 8h12M9 3l5 5-5 5"/></svg></a>
  <div class="abs product-photo" role="img" aria-label="Schwarzes Mainboard mit Prozessorsockel und orangefarbenen Leiterbahnen"></div>
  <svg class="abs slider-arrow slider-next" viewBox="0 0 20 28" fill="none" stroke="#ff6a00" stroke-width="3.5"><path d="M5 3l10 11L5 25"/></svg>
</section>

<section class="section philosophy">
  <h2 class="abs section-title">Unsere Philosophie</h2>
  <div class="abs philosophy-text">
    <p>Als mittelständisches inhabergeführtes Unternehmen ist es unser Ziel entgegen dem Trend der Wegwerfgesellschaft, langlebige Produkte anzubieten, welche eine ausgewogene Preis-Leistung aufweisen. Deshalb ist bei uns eine eine 5-Jährige Zufriedenheitsgarantie selbstverständlich.</p>
    <p>Wir pflegen eine offene und ehrliche Kommunikation mit unseren Kunden, daher haben wir Ihnen zum Beispiel auf der folgenden Seite einige Hinweise zum Hinterfragen von <a>One-Stop-Angeboten</a> aufgezeigt.</p>
  </div>
</section>

<footer class="section site-footer">
  <div class="abs footer-brand">Trusk Halvorsen</div>
  <div class="abs social"><span aria-label="Soziales Netzwerk"></span><span aria-label="Soziales Netzwerk"></span></div>
  <div class="abs footer-info">
    <p><strong>Trusk Halvorsen GmbH &amp; Co. KG</strong></p>
    <p>Lindenweg 8<br>86930 Mühlbach</p>
    <p>Mobile +49 (0) 8341 5520 418<br>Telefon +49 (0) 8341 5520 418<br>Fax +49 (0) 8341 5520 41</p>
    <p>kontakt@trusk-halvorsen.de</p>
    <div class="footer-links"><span>Impressum</span><span>Datenschutzerklärung</span></div>
  </div>
  <div class="abs map" role="img" aria-label="Dunkle Straßenkarte rund um den Firmenstandort">
    <div class="abs map-label">Lindenweg 8<br>86930 Mühlbach<br><span>Im Kartendienst anzeigen</span></div>
  </div>
</footer>

</body>
</html>
```